Marisa Dee Creations & Affairs business card

I need an elegant informative but not busy business card using my logo. We are a florist with high end customers. I am adding a PDF file and a PNG file for those who requested it

Reason: still working on changes

Reason: Working on changes

Reason: making changes

Target Market(s)

Brides, grooms, men purchasing flowers
Ages 20-65

Industry/Entity Type

Florist

Requirements
Must have
• Business info:
Marisa Dee Creation & Affairs
www.marisadeeaffairs.example.
555-418-7362

555-418-7362
Nice to have
• Est 1954
may want Pinterest logo, twitter and linkedin and facbook
Should not have
• Clip art or photos

```html
<!DOCTYPE html>
<html lang="en">
<head>
<meta charset="utf-8">
<title>Marisa Dee Creations &amp; Affairs — Business Card</title>
<link rel="stylesheet" href="https://fonts.googleapis.com/css2?family=Cinzel:wght@400;500&family=Questrial&display=swap">
<style>
  :root {
    --backdrop: #ecebea;
    --pink: #f4a9b7;
    --pink-deep: #ee9aab;
    --pink-soft: #f7b9c4;
    --pink-line: #f0a3b2;
    --card-white: #ffffff;
    --ink: #2b2b2b;
    --white: #ffffff;
  }
  * { margin: 0; padding: 0; box-sizing: border-box; }
  html, body {
    width: 1200px; height: 941px; overflow: hidden;
    background: var(--backdrop);
  }
  .stage {
    position: relative; width: 1200px; height: 941px;
    display: flex; justify-content: center; align-items: center; gap: 90px;
  }
  .card {
    position: relative; width: 340px; height: 595px;
    box-shadow: 0 6px 18px rgba(0,0,0,.12);
    overflow: hidden;
  }

  /* Front */
  .card-front {
    background: linear-gradient(160deg, var(--pink-soft), var(--pink) 55%, var(--pink-deep));
  }
  .swirl-band {
    position: absolute; left: 0; width: 100%; height: 150px;
    background: linear-gradient(180deg, rgba(238,150,168,.35), rgba(238,150,168,.15));
  }
  .swirl-band.top { top: 0; }
  .swirl-band.bottom { bottom: 0; background: linear-gradient(0deg, rgba(238,150,168,.35), rgba(238,150,168,.15)); }
  .front-brand {
    position: absolute; top: 210px; left: 0; width: 100%;
    text-align: center; color: var(--white);
  }
  .brand-mark {
    display: block; width: 44px; height: 44px; margin: 0 auto 14px;
    border: 2px solid var(--white); border-radius: 50%;
  }
  .brand-name {
    font-family: "Cinzel", serif; font-weight: 400;
    font-size: 40px; letter-spacing: 3px; line-height: 1;
  }
  .brand-tagline {
    font-family: "Cinzel", serif; font-weight: 400;
    font-size: 12px; letter-spacing: 4.5px; margin-top: 8px;
  }

  /* Back */
  .card-back { background: linear-gradient(180deg, var(--card-white), #f6f6f6); }
  .divider {
    position: absolute; left: 30px; width: 280px; height: 30px;
    display: flex; align-items: center; gap: 12px;
  }
  .divider.top { top: 70px; }
  .divider.bottom { bottom: 70px; }
  .divider-line { flex: 1; height: 3px; background: var(--pink-line); }
  .divider-bud {
    width: 30px; height: 26px; border-radius: 50%;
    background: var(--pink-soft); opacity: .7;
  }
  .back-info {
    position: absolute; top: 230px; left: 0; width: 100%;
    text-align: center; color: var(--ink);
  }
  .company-name {
    font-family: "Cinzel", serif; font-weight: 400;
    font-size: 15px; letter-spacing: .6px;
  }
  .social-row {
    display: flex; justify-content: center; gap: 10px; margin: 26px 0 10px;
  }
  .social-box { width: 20px; height: 20px; background: var(--pink-line); }
  .contact-line {
    font-family: "Questrial", sans-serif; font-size: 13px;
    letter-spacing: .3px; line-height: 26px;
  }
</style>
</head>
<body>
  <main class="stage">
    <section class="card card-front" aria-label="Card front">
      <div class="swirl-band top" role="img" aria-label="Faint pink swirl pattern"></div>
      <div class="swirl-band bottom" role="img" aria-label="Faint pink swirl pattern"></div>
      <div class="front-brand">
        <span class="brand-mark" aria-hidden="true"></span>
        <h1 class="brand-name">Marisa Dee</h1>
        <p class="brand-tagline">CREATIONS &amp; AFFAIRS</p>
      </div>
    </section>

    <section class="card card-back" aria-label="Card back">
      <div class="divider top">
        <span class="divider-line"></span>
        <span class="divider-bud" role="img" aria-label="Small rosebud ornament"></span>
        <span class="divider-line"></span>
      </div>
      <div class="back-info">
        <h2 class="company-name">Marisa Dee Creation &amp; Affairs</h2>
        <div class="social-row" aria-label="Social profiles">
          <span class="social-box"></span>
          <span class="social-box"></span>
          <span class="social-box"></span>
        </div>
        <p class="contact-line">555-418-7362</p>
        <p class="contact-line">www.marisadeeaffairs.example.</p>
      </div>
      <div class="divider bottom">
        <span class="divider-line"></span>
        <span class="divider-bud" role="img" aria-label="Small rosebud ornament"></span>
        <span class="divider-line"></span>
      </div>
    </section>
  </main>
</body>
</html>
```